Design packaging for a line of cell phone accessories

Hello,
we are seeking to develop the footprint for a line of cellphone accessories and gadgets. It will regard packaging for amongst others :
-bluetooth headphones
-powercases
-chargers
-Shopping bags
-cases
-cable
-etc
The entire line should carry the same design, but will obviously involve different product/sizes/specs. It's about the most original FOOTPRINT!!
The logo is attached
The design should contain the main colors: Orange on Black
I also added a die-cut and image of a product (solar charger) which should be redesigned per the above specifics

Industry/Entity Type

Cell Phone

Requirements
Must have
• Gold on black

```html
<!DOCTYPE html>
<html lang="en">
<head>
<meta charset="UTF-8">
<title>Solar Charger – Packaging Spine and Front Panel</title>
<link rel="stylesheet" href="https://fonts.googleapis.com/css2?family=Baloo+2:wght@400;800&family=Quicksand:wght@500;600&display=swap">
<style>
  :root {
    --orange: #e2692a;
    --orange-deep: #c4551c;
    --black: #0e0e0e;
    --charcoal: #2a2a2a;
    --grey-light: #d9d9d9;
    --white: #ffffff;
    --page: #f2f2f2;
  }
  * { box-sizing: border-box; margin: 0; padding: 0; }
  html, body { width: 1200px; height: 1200px; overflow: hidden; background: var(--page); }
  .canvas { position: relative; width: 1200px; height: 1200px; }

  /* ---------- Spine ---------- */
  .spine-panel {
    position: absolute; left: 180px; top: 40px;
    width: 140px; height: 1120px;
    background: var(--orange);
    overflow: hidden;
  }
  .spine-cap {
    position: absolute; left: 0; top: 0; width: 100%; height: 100px;
    background: linear-gradient(180deg, #f4f4f4 0%, var(--grey-light) 100%);
  }
  .spine-cap-line {
    position: absolute; left: 0; top: 60px; width: 100%; height: 6px; background: var(--black);
  }
  .spine-rule { position: absolute; left: 0; width: 100%; height: 6px; background: var(--black); }
  .spine-rule--top { top: 100px; }
  .spine-rule--upper { top: 310px; }
  .spine-rule--lower { top: 1000px; }
  .spine-rule--base { top: 1080px; }
  .spine-edge {
    position: absolute; right: 0; top: 100px; width: 14px; height: 980px; background: var(--black);
  }
  .spine-title {
    position: absolute; left: 70px; top: 660px;
    transform: translate(-50%, -50%) rotate(90deg);
    white-space: nowrap;
    font-family: "Baloo 2", sans-serif; font-weight: 800;
    font-size: 72px; line-height: 1; color: var(--black);
  }

  /* ---------- Front ---------- */
  .front-panel {
    position: absolute; left: 320px; top: 40px;
    width: 700px; height: 1120px;
    background: var(--black);
    overflow: hidden;
  }
  .texture-band {
    position: absolute; left: 0; top: 0; width: 100%; height: 100px;
    background: linear-gradient(180deg, #1a1a1a 0%, #3a3a3a 50%, #1a1a1a 100%);
  }
  .texture-band-tab {
    position: absolute; left: 0; top: 0; width: 200px; height: 60px;
    background: linear-gradient(180deg, #f4f4f4 0%, var(--grey-light) 100%);
  }
  .cable-note-area {
    position: absolute; left: 0; top: 100px; width: 100%; height: 210px;
    background: linear-gradient(180deg, var(--white) 0%, #ececec 100%);
  }
  .cable-note {
    position: absolute; left: 30px; top: 125px; width: 320px;
    font-family: "Quicksand", sans-serif; font-weight: 600;
    font-size: 24px; line-height: 1.05; text-align: center; color: var(--charcoal);
  }
  .grid-field {
    position: absolute; left: 0; top: 310px; width: 100%; height: 690px;
    background: radial-gradient(ellipse at 35% 45%, #f4f4f4 0%, #a9a9a9 35%, #3b3b3b 70%, #111 100%);
  }
  .frame-line { position: absolute; background: var(--orange); }
  .frame-line--top { left: 0; top: 310px; width: 100%; height: 6px; }
  .frame-line--left { left: 18px; top: 316px; width: 6px; height: 684px; }

  .product-photo {
    position: absolute; left: 360px; top: 160px; width: 330px; height: 620px;
    border-radius: 36px;
    background: linear-gradient(160deg, #3a3a3a 0%, #151515 60%, #050505 100%);
  }

  .product-title {
    position: absolute; left: 20px; top: 790px; width: 440px;
    font-family: "Baloo 2", sans-serif; font-weight: 800;
    font-size: 108px; line-height: 0.9; text-align: center;
    color: var(--orange);
    -webkit-text-stroke: 5px var(--black);
    paint-order: stroke fill;
  }

  .brand {
    position: absolute; left: 475px; top: 905px;
    display: flex; align-items: center; gap: 10px;
  }
  .brand-dot { width: 30px; height: 30px; border-radius: 50%; background: var(--orange); }
  .brand-name {
    font-family: "Quicksand", sans-serif; font-weight: 600;
    font-size: 24px; color: var(--white); letter-spacing: 1px; line-height: 1;
  }
  .brand-tagline {
    font-family: "Quicksand", sans-serif; font-weight: 600;
    font-size: 12px; color: var(--white); margin-top: 3px;
  }

  .feature-bar {
    position: absolute; left: 0; top: 1000px; width: 100%; height: 80px;
    background: var(--black);
  }
  .feature-stripe {
    position: absolute; top: 1026px; height: 28px; background: var(--orange);
  }
  .feature-stripe--left { left: 0; width: 33px; }
  .feature-stripe--right { left: 376px; width: 324px; }
  .feature-label {
    position: absolute; left: 33px; top: 1000px; width: 343px; height: 80px;
    background: var(--black);
    font-family: "Baloo 2", sans-serif; font-weight: 400;
    font-size: 52px; line-height: 80px; text-align: center; color: var(--orange);
  }
  .base-band {
    position: absolute; left: 0; top: 1080px; width: 100%; height: 40px;
    background: linear-gradient(180deg, var(--orange) 0%, var(--orange-deep) 100%);
  }
</style>
</head>
<body>
<div class="canvas">
  <aside class="spine-panel">
    <div class="spine-cap"></div>
    <div class="spine-cap-line"></div>
    <div class="spine-rule spine-rule--top"></div>
    <div class="spine-rule spine-rule--upper"></div>
    <div class="spine-rule spine-rule--lower"></div>
    <div class="spine-rule spine-rule--base"></div>
    <div class="spine-edge"></div>
    <p class="spine-title">Solar Charger</p>
  </aside>

  <section class="front-panel">
    <div class="texture-band" role="img" aria-label="Dark textured pattern band"></div>
    <div class="texture-band-tab"></div>
    <div class="cable-note-area"></div>
    <p class="cable-note">Including multi cable<br>for all smart devices and<br>micro-USB</p>

    <div class="grid-field" role="img" aria-label="Dark metallic grid pattern with bright centre glow"></div>
    <div class="frame-line frame-line--top"></div>
    <div class="frame-line frame-line--left"></div>

    <div class="product-photo" role="img" aria-label="Product photo of the black solar charger with connector plug"></div>

    <h1 class="product-title">Solar<br>Charger</h1>

    <div class="brand">
      <span class="brand-dot"></span>
      <div>
        <div class="brand-name">VOLTARA</div>
        <div class="brand-tagline">Accessories and gadgets</div>
      </div>
    </div>

    <div class="feature-bar"></div>
    <div class="feature-stripe feature-stripe--left"></div>
    <div class="feature-stripe feature-stripe--right"></div>
    <p class="feature-label">with USB out</p>
    <div class="base-band"></div>
  </section>
</div>
</body>
</html>
```